2in1 Bartender & Sommelier needs a business card

I need a business card. I worked as a bartender in many places but I just finished a sommelier school and I would like a new business card. I like minimal design, natural materials and something what makes the people think :) I try to be creative in cocktail making, like little mixology, little twist on recipes... I like to travel and discover new places, cultures and of course interesting drinks and improve continously...live a little bit crazy life. And I like what I do...

Target Market(s)

restaurant/winebar managers, winemakers, other sommeliers and bartenders, people who work in food and beverage sector

Industry/Entity Type

Hospitality

Contact Information for Business Card

Rozsa Tarkany
Bartender & Sommelier
Phone: (FR) +33 6 4827 3190
(HU) +36 70 918 6352

Font styles to use
Script

Requirements
Must have
• Some sign, I am a bartender and sommelier as well.
Nice to have
• black and white maybe with 1 or 2 extra color
Should not have
• very colourful, to many things on the card

```html
<!DOCTYPE html>
<html lang="en">
<head>
<meta charset="utf-8">
<title>Rozsa Tarkany – Business Card</title>
<link rel="stylesheet" href="https://fonts.googleapis.com/css2?family=Great+Vibes&family=Open+Sans:wght@300;400&display=swap">
<style>
  :root {
    --page-bg: #dcdfe0;
    --card-bg: #ffffff;
    --ink-soft: #8a8a8a;
    --ink-mid: #757575;
    --ink-dark: #4a4a4a;
    --rule: #6f6f6f;
  }
  html, body {
    margin: 0;
    padding: 0;
    width: 1200px;
    height: 1000px;
    overflow: hidden;
    background: var(--page-bg);
  }
  .card {
    position: absolute;
    left: 100px;
    top: 200px;
    width: 1000px;
    height: 600px;
    background: var(--card-bg);
    box-shadow: 0 6px 24px rgba(0,0,0,0.12);
  }
  .emblem {
    position: absolute;
    left: 95px;
    top: 125px;
    width: 115px;
    height: 347px;
  }
  .holder-name {
    position: absolute;
    left: 303px;
    top: 158px;
    width: 600px;
    margin: 0;
    text-align: center;
    font-family: "Great Vibes", cursive;
    font-weight: 400;
    font-size: 50px;
    line-height: 70px;
    color: var(--ink-soft);
  }
  .holder-role {
    position: absolute;
    left: 289px;
    top: 250px;
    width: 626px;
    margin: 0;
    text-align: center;
    font-family: "Open Sans", sans-serif;
    font-weight: 400;
    font-size: 25px;
    line-height: 30px;
    letter-spacing: 0.36em;
    color: var(--ink-mid);
  }
  .divider {
    position: absolute;
    left: 289px;
    top: 294px;
    width: 626px;
    height: 3px;
    background: var(--rule);
  }
  .contact {
    position: absolute;
    left: 387px;
    top: 388px;
    display: flex;
    align-items: center;
    gap: 15px;
  }
  .contact-icon {
    width: 40px;
    height: 40px;
    flex: none;
  }
  .contact-lines {
    font-family: "Open Sans", sans-serif;
    font-weight: 400;
    font-size: 25px;
    line-height: 36px;
    color: var(--ink-soft);
  }
</style>
</head>
<body>
  <main class="card">
    <svg class="emblem" viewBox="0 0 115 347" role="img" aria-label="Line-drawn wine glass with a swirling pour mark">
      <defs>
        <linearGradient id="emblemTone" x1="0" y1="0" x2="0" y2="1">
          <stop offset="0" stop-color="#b5b5b5"/>
          <stop offset="1" stop-color="#555555"/>
        </linearGradient>
      </defs>
      <rect x="0" y="0" width="115" height="347" fill="url(#emblemTone)" opacity="0.55"/>
    </svg>

    <h1 class="holder-name">Rozsa Tarkany</h1>
    <p class="holder-role">Bartender &amp; Sommelier</p>
    <div class="divider"></div>

    <div class="contact">
      <svg class="contact-icon" viewBox="0 0 40 40" aria-hidden="true">
        <circle cx="20" cy="20" r="20" fill="var(--ink-soft)"/>
        <path d="M14.2 11.5c.8-.6 1.8-.4 2.3.4l1.8 2.9c.4.7.3 1.6-.3 2.1l-1.3 1.1c.9 2 2.6 3.8 4.6 4.8l1.1-1.3c.5-.6 1.4-.8 2.1-.3l2.9 1.8c.8.5 1 1.5.4 2.3l-1.2 1.5c-.8 1-2.2 1.4-3.4.9-5.3-2-9.2-5.9-11.2-11.2-.5-1.2-.1-2.6.9-3.4z" fill="#ffffff"/>
      </svg>
      <div class="contact-lines">
        <div class="phone">(FR) +33 6 4827 3190</div>
        <div class="phone">(HU) +36 70 918 6352</div>
      </div>
    </div>
  </main>
</body>
</html>
```